Broschüre für Sicherheitsdienstleistungen
Zielgruppe
Sicherheitsunternehmen
Hallo,
Wir möchten gerne eine Broschüre (ca. 12 Seiten) gestalten lassen wo alle unsere verschiedene Dienstleistungen Beschrieben werden und unser unternehmen vorgestellt wird an den Kunden.
Als Hard copy Version von unsere neue Seite : http://kwt.seitenplanung-beispiel.de
Das Design soll Freundlich und Modern Gestaltet werden.
Farbtöne gerne in Weiss und Dunkel Blau
Produktdetails :
Rückendrahtheftung links, 4/4-farbig (beidseitiger Druck, CMYK)
ab 250 g wird der Umschlag zusätzlich genutet
Veredelung Umschlag
beidseitiger UV-Lack glänzend
Format
DIN A4 (21 x 29,7 cm)
Details: Hochformat
Seitenanzahl ca. 10 - 12 (Excl. Umschlag)
Material Umschlag
250g Bilderdruck glänzend
New Website Design :
http://kwt.seitenplanung-beispiel.de

```html
<!DOCTYPE html>
<html lang="de">
<head>
<meta charset="utf-8">
<title>Kontakt</title>
<link rel="stylesheet" href="https://fonts.googleapis.com/css2?family=Fira+Sans:wght@400;600&family=Fira+Sans+Condensed:wght@600&display=swap">
<style>
  :root {
    --navy: #44617f;
    --row-bg: #eaeef1;
    --ink: #1f1f1f;
    --paper: #ffffff;
  }
  * { margin: 0; padding: 0; box-sizing: border-box; }
  html, body { width: 849px; height: 1200px; overflow: hidden; background: var(--paper); }
  .page {
    position: relative;
    width: 849px; height: 1200px;
    font-family: "Fira Sans", Arial, sans-serif;
    font-feature-settings: "onum" 1;
    color: var(--ink);
  }
  .corner-tab {
    position: absolute; left: 51px; top: 0;
    width: 42px; height: 51px; background: var(--navy);
  }
  .page-title {
    position: absolute; left: 51px; top: 88px;
    font-family: "Fira Sans Condensed", "Fira Sans", sans-serif;
    font-weight: 600; font-size: 35px; color: var(--navy);
    letter-spacing: 0.2px;
  }
  .contact-row {
    position: absolute; left: 51px; width: 741px;
    background: var(--row-bg);
    display: flex; align-items: center;
  }
  .contact-icon {
    width: 29px; height: 100%;
    background: var(--navy);
    display: flex; align-items: center; justify-content: center;
    flex: none;
  }
  .contact-icon svg { width: 16px; height: 16px; fill: #fff; }
  .contact-text {
    margin-left: 37px;
    font-size: 16px; line-height: 24px;
  }
  .row-address { top: 215px; height: 57px; }
  .row-phone   { top: 292px; height: 29px; }
  .row-mail    { top: 341px; height: 29px; }
  .row-hours   { top: 390px; height: 57px; }
  .brand {
    position: absolute; left: 0; width: 849px; top: 560px;
    display: flex; justify-content: center; align-items: center; gap: 12px;
  }
  .brand-mark { width: 22px; height: 22px; background: var(--navy); }
  .brand-name {
    font-family: "Fira Sans", Arial, sans-serif;
    font-weight: 600; font-size: 34px; color: var(--navy);
    letter-spacing: 1px;
  }
  .river-photo {
    position: absolute; left: 51px; top: 630px;
    width: 739px; height: 474px;
    background:
      linear-gradient(to bottom, rgba(255,255,255,0) 0%, rgba(255,255,255,0) 50%, rgba(90,170,200,0.35) 70%, rgba(60,140,180,0.45) 100%),
      linear-gradient(to right, #3c78b3 0%, #7fb0d2 40%, #c9d5cf 65%, #f3c85a 88%, #f7d46e 100%);
  }
  .footer-band {
    position: absolute; left: 51px; top: 1104px;
    width: 739px; height: 35px; background: var(--navy);
  }
</style>
</head>
<body>
<div class="page">
  <div class="corner-tab"></div>
  <h1 class="page-title">Kontakt</h1>

  <div class="contact-row row-address">
    <div class="contact-icon">
      <svg viewBox="0 0 16 16" aria-hidden="true"><path d="M8 1.5 0.5 8h2.2v6.5h4V10h2.6v4.5h4V8h2.2z"/></svg>
    </div>
    <p class="contact-text">Lindenhofweg 14<br>50321 Rheinfeld</p>
  </div>

  <div class="contact-row row-phone">
    <div class="contact-icon">
      <svg viewBox="0 0 16 16" aria-hidden="true"><path d="M3.6 1 6 3.6 4.7 5.6c.9 2.2 2.9 4.3 5.2 5.3l2-1.3L14.5 12 13 14.6C6.8 14.3 1.6 9.2 1.3 2.8z"/></svg>
    </div>
    <p class="contact-text">0800 417 2086</p>
  </div>

  <div class="contact-row row-mail">
    <div class="contact-icon">
      <svg viewBox="0 0 16 16" aria-hidden="true"><path d="M1 3.5h14v1.2L8 9 1 4.7zM1 6.3l7 4.3 7-4.3v6.2H1z"/></svg>
    </div>
    <p class="contact-text">Info@wachwerk-beispiel.de</p>
  </div>

  <div class="contact-row row-hours">
    <div class="contact-icon">
      <svg viewBox="0 0 16 16" aria-hidden="true"><path d="M8 1a7 7 0 1 0 0 14A7 7 0 0 0 8 1zm0 1.8a5.2 5.2 0 1 1 0 10.4A5.2 5.2 0 0 1 8 2.8zM7.2 4.5v4.3h3.5V7.6H8.4V4.5z"/></svg>
    </div>
    <p class="contact-text">Mo. – Fr. 9.00 – 18.00 Uhr<br>und nach Vereinbarung</p>
  </div>

  <div class="river-photo" role="img" aria-label="Foto: Flussufer mit Stadtsilhouette, Fernsehturm und Brücke bei Sonnenuntergang"></div>

  <div class="brand">
    <span class="brand-mark"></span>
    <span class="brand-name">Wachwerk</span>
  </div>

  <div class="footer-band"></div>
</div>
</body>
</html>
```